Quiz Company needs two PDF sheets designing

We need two different A4 sheets to be designed - similar to those attached - they need to be at least two-coloured - A4 horizontal layout

The Bingo sheet is as per the attached Word mock up and is similar to the Bingo PDF attached

The Cellraiders sheet should feature 24 hexagons in 6 vertical rows of 4 hexagons

Font styles to use
Serif

Requirements
Must have
• PDF file at least two colours
• www.marlowtrivet.co.uk - 01632 960481 and our logo somewhere on the sheet
Nice to have
• Right Hand Side - Bingo - A Six x Six Grid of round squares with space to write numbers and answers in
• Left Hand side - Space for instructions Numbers 1 to 36 with space for answers - then a mini grid with just circles and space to write numbers in see attached mock up.
• Cellraiders - Right hand side will be 6 lines of 4 hexagons all connecting as per the example - top left numbers 1 to 24 and a small grid for just numbers
• Both sheets also have instructions

```html
<!DOCTYPE html>
<html lang="en">
<head>
<meta charset="utf-8">
<title>Quiz Sheets – Marlow Trivet</title>
<link href="https://fonts.googleapis.com/css2?family=PT+Serif:wght@400;700&display=swap" rel="stylesheet">
<style>
:root{
  --ink:#6064ae;
  --ink-soft:#7478c0;
  --dot-light:#c4c4fa;
  --dot-dark:#a9a9ee;
  --paper:#ffffff;
}
*{box-sizing:border-box;margin:0;padding:0}
html,body{width:1200px;height:1090px;overflow:hidden;background:var(--paper)}
body{font-family:"PT Serif",Georgia,serif;color:var(--ink)}

.sheet{position:relative;width:1200px;height:1090px;overflow:hidden;background:var(--paper)}

/* Screen shows the bingo sheet; print produces both A4 sheets */
@media screen{.sheet-cellraiders{display:none}}
@page{size:1200px 1090px;margin:0}
@media print{
  html,body{height:auto;overflow:visible}
  .sheet{page-break-after:always;break-after:page}
}

/* Tear-off answer strip */
.answer-strip{position:absolute;left:6px;top:8px;width:312px;height:750px;border:1.5px solid var(--ink-soft);padding:8px 11px}
.answer-strip.short{height:510px}
.answer-row{height:16px;border:1px solid var(--ink-soft);margin-bottom:3.95px;font-size:8.5px;font-weight:700;padding-left:8px;line-height:14px}
.answer-row.team{letter-spacing:.5px;font-size:9px;margin-bottom:4.6px}
.number-grid{position:absolute;left:6px;top:769px;width:311px;height:313px;display:grid;grid-template-columns:repeat(6,1fr);grid-template-rows:repeat(6,1fr);border:1px solid var(--ink-soft)}
.number-grid.four-rows{top:530px;height:210px;grid-template-rows:repeat(4,1fr)}
.number-grid span{border:.5px solid var(--ink-soft)}

.tear-line{position:absolute;left:333px;top:0;height:1090px;border-left:2px dashed #222}

/* Header */
.brand{position:absolute;left:364px;top:24px;width:226px;height:44px;display:flex;align-items:center;justify-content:center;gap:8px}
.brand-dot{width:18px;height:18px;border-radius:50%;background:var(--ink)}
.brand-name{font-size:22px;font-weight:700;color:var(--ink)}
.contact{position:absolute;left:354px;width:246px;text-align:center;font-weight:700}
.contact.web{top:74px;font-size:18px}
.contact.tel{top:99px;font-size:17px;font-weight:400}
.title-box{position:absolute;left:926px;top:26px;width:252px;height:85px;background:var(--ink);color:#fff;font-size:40px;font-weight:700;display:flex;align-items:center;justify-content:center;white-space:nowrap}
.title-box.wide{font-size:36px}

.instructions{position:absolute;left:354px;top:130px;width:834px;font-size:9.3px;font-weight:700;line-height:14px}
.team-name{position:absolute;left:354px;top:196px;font-size:16px;font-weight:700;letter-spacing:.3px}
.team-line{position:absolute;left:463px;top:214px;width:681px;border-top:1.5px solid var(--ink)}

/* Bingo board */
.bingo-board{position:absolute;left:353px;top:236px;width:841px;height:846px;display:grid;grid-template-columns:repeat(6,1fr);grid-template-rows:repeat(6,1fr);border:2.5px solid var(--ink)}
.bingo-cell{border:1.25px solid var(--ink);position:relative}
.bingo-cell::before{content:"";position:absolute;left:10px;top:8px;width:46px;height:46px;border-radius:50%;background:radial-gradient(circle at 40% 35%,var(--dot-light),var(--dot-dark))}

/* Cellraiders board */
.hex-board{position:absolute;left:353px;top:270px;width:841px;height:700px}
.hex-cell{fill:var(--paper);stroke:var(--ink);stroke-width:2.5}
.hex-number{fill:var(--ink);font-family:"PT Serif",Georgia,serif;font-size:15px;font-weight:700}
</style>
</head>
<body>

<!-- Sheet 1: Quiz Bingo -->
<section class="sheet sheet-bingo">
  <div class="answer-strip">
    <div class="answer-row team">TEAM NAME:</div>
    <div class="answer-row">1</div><div class="answer-row">2</div><div class="answer-row">3</div><div class="answer-row">4</div>
    <div class="answer-row">5</div><div class="answer-row">6</div><div class="answer-row">7</div><div class="answer-row">8</div>
    <div class="answer-row">9</div><div class="answer-row">10</div><div class="answer-row">11</div><div class="answer-row">12</div>
    <div class="answer-row">13</div><div class="answer-row">14</div><div class="answer-row">15</div><div class="answer-row">16</div>
    <div class="answer-row">17</div><div class="answer-row">18</div><div class="answer-row">19</div><div class="answer-row">20</div>
    <div class="answer-row">21</div><div class="answer-row">22</div><div class="answer-row">23</div><div class="answer-row">24</div>
    <div class="answer-row">25</div><div class="answer-row">26</div><div class="answer-row">27</div><div class="answer-row">28</div>
    <div class="answer-row">29</div><div class="answer-row">30</div><div class="answer-row">31</div><div class="answer-row">32</div>
    <div class="answer-row">33</div><div class="answer-row">34</div><div class="answer-row">35</div><div class="answer-row">36</div>
  </div>

  <div class="number-grid">
    <span></span><span></span><span></span><span></span><span></span><span></span>
    <span></span><span></span><span></span><span></span><span></span><span></span>
    <span></span><span></span><span></span><span></span><span></span><span></span>
    <span></span><span></span><span></span><span></span><span></span><span></span>
    <span></span><span></span><span></span><span></span><span></span><span></span>
    <span></span><span></span><span></span><span></span><span></span><span></span>
  </div>

  <div class="tear-line"></div>

  <div class="brand"><span class="brand-dot"></span><span class="brand-name">Marlow Trivet</span></div>
  <div class="contact web">www.marlowtrivet.co.uk</div>
  <div class="contact tel">Tel: 01632 960481</div>

  <div class="title-box">Quiz Bingo</div>

  <p class="instructions">The quiz master will call out questions from 1 to 36 – write the number of the question and the answer to it in ANY circle above and copy the answer against the correct number above left. Also write the numbers you use in the corresponding circles bottom left. Once all questions have been read out, tear off the left hand side and hand to the quizmaster. They will now read out the answers in a random order – you need to get a straight line of six correct answers – once you have them shout “HOUSE” and the quizmaster will check your sheet – Good Luck – anyone seen with a mobile phone will have it smashed to pieces with a hammer and will be disqualified!</p>

  <div class="team-name">TEAM NAME:</div>
  <div class="team-line"></div>

  <div class="bingo-board">
    <div class="bingo-cell"></div><div class="bingo-cell"></div><div class="bingo-cell"></div><div class="bingo-cell"></div><div class="bingo-cell"></div><div class="bingo-cell"></div>
    <div class="bingo-cell"></div><div class="bingo-cell"></div><div class="bingo-cell"></div><div class="bingo-cell"></div><div class="bingo-cell"></div><div class="bingo-cell"></div>
    <div class="bingo-cell"></div><div class="bingo-cell"></div><div class="bingo-cell"></div><div class="bingo-cell"></div><div class="bingo-cell"></div><div class="bingo-cell"></div>
    <div class="bingo-cell"></div><div class="bingo-cell"></div><div class="bingo-cell"></div><div class="bingo-cell"></div><div class="bingo-cell"></div><div class="bingo-cell"></div>
    <div class="bingo-cell"></div><div class="bingo-cell"></div><div class="bingo-cell"></div><div class="bingo-cell"></div><div class="bingo-cell"></div><div class="bingo-cell"></div>
    <div class="bingo-cell"></div><div class="bingo-cell"></div><div class="bingo-cell"></div><div class="bingo-cell"></div><div class="bingo-cell"></div><div class="bingo-cell"></div>
  </div>
</section>

<!-- Sheet 2: Cellraiders -->
<section class="sheet sheet-cellraiders">
  <div class="answer-strip short">
    <div class="answer-row team">TEAM NAME:</div>
    <div class="answer-row">1</div><div class="answer-row">2</div><div class="answer-row">3</div><div class="answer-row">4</div>
    <div class="answer-row">5</div><div class="answer-row">6</div><div class="answer-row">7</div><div class="answer-row">8</div>
    <div class="answer-row">9</div><div class="answer-row">10</div><div class="answer-row">11</div><div class="answer-row">12</div>
    <div class="answer-row">13</div><div class="answer-row">14</div><div class="answer-row">15</div><div class="answer-row">16</div>
    <div class="answer-row">17</div><div class="answer-row">18</div><div class="answer-row">19</div><div class="answer-row">20</div>
    <div class="answer-row">21</div><div class="answer-row">22</div><div class="answer-row">23</div><div class="answer-row">24</div>
  </div>

  <div class="number-grid four-rows">
    <span></span><span></span><span></span><span></span><span></span><span></span>
    <span></span><span></span><span></span><span></span><span></span><span></span>
    <span></span><span></span><span></span><span></span><span></span><span></span>
    <span></span><span></span><span></span><span></span><span></span><span></span>
  </div>

  <div class="tear-line"></div>

  <div class="brand"><span class="brand-dot"></span><span class="brand-name">Marlow Trivet</span></div>
  <div class="contact web">www.marlowtrivet.co.uk</div>
  <div class="contact tel">Tel: 01632 960481</div>

  <div class="title-box wide">Cellraiders</div>

  <p class="instructions">The quiz master will call out questions from 1 to 24 – write the answer to each question in the hexagon with the matching number and copy the answer against the correct number above left. Once all questions have been read out, tear off the left hand side and hand it to the quizmaster. They will now read out the answers in a random order – mark each correct hexagon in the small grid bottom left. You need a chain of touching hexagons running from one side of the board to the other – once you have one shout “CELL” and the quizmaster will check your sheet – Good Luck – anyone seen with a mobile phone will be disqualified!</p>

  <div class="team-name">TEAM NAME:</div>
  <div class="team-line"></div>

  <svg class="hex-board" viewBox="0 0 841 700" aria-label="Board of 24 numbered hexagons">
    <defs>
      <polygon id="hex" class="hex-cell" points="-88,0 -44,-76.2 44,-76.2 88,0 44,76.2 -44,76.2"/>
    </defs>
    <use href="#hex" x="88" y="76.2"/><use href="#hex" x="88" y="228.6"/><use href="#hex" x="88" y="381"/><use href="#hex" x="88" y="533.4"/>
    <use href="#hex" x="220" y="152.4"/><use href="#hex" x="220" y="304.8"/><use href="#hex" x="220" y="457.2"/><use href="#hex" x="220" y="609.6"/>
    <use href="#hex" x="352" y="76.2"/><use href="#hex" x="352" y="228.6"/><use href="#hex" x="352" y="381"/><use href="#hex" x="352" y="533.4"/>
    <use href="#hex" x="484" y="152.4"/><use href="#hex" x="484" y="304.8"/><use href="#hex" x="484" y="457.2"/><use href="#hex" x="484" y="609.6"/>
    <use href="#hex" x="616" y="76.2"/><use href="#hex" x="616" y="228.6"/><use href="#hex" x="616" y="381"/><use href="#hex" x="616" y="533.4"/>
    <use href="#hex" x="748" y="152.4"/><use href="#hex" x="748" y="304.8"/><use href="#hex" x="748" y="457.2"/><use href="#hex" x="748" y="609.6"/>

    <text class="hex-number" x="52" y="38">1</text><text class="hex-number" x="52" y="190">2</text><text class="hex-number" x="52" y="343">3</text><text class="hex-number" x="52" y="495">4</text>
    <text class="hex-number" x="184" y="114">5</text><text class="hex-number" x="184" y="267">6</text><text class="hex-number" x="184" y="419">7</text><text class="hex-number" x="184" y="572">8</text>
    <text class="hex-number" x="316" y="38">9</text><text class="hex-number" x="316" y="190">10</text><text class="hex-number" x="316" y="343">11</text><text class="hex-number" x="316" y="495">12</text>
    <text class="hex-number" x="448" y="114">13</text><text class="hex-number" x="448" y="267">14</text><text class="hex-number" x="448" y="419">15</text><text class="hex-number" x="448" y="572">16</text>
    <text class="hex-number" x="580" y="38">17</text><text class="hex-number" x="580" y="190">18</text><text class="hex-number" x="580" y="343">19</text><text class="hex-number" x="580" y="495">20</text>
    <text class="hex-number" x="712" y="114">21</text><text class="hex-number" x="712" y="267">22</text><text class="hex-number" x="712" y="419">23</text><text class="hex-number" x="712" y="572">24</text>
  </svg>
</section>

</body>
</html>
```